Business Cards & Stationery for a Gold Refiner
Brambleton Assets
Business Cards & Stationery for a Gold Refiner - Jewelry
Creative Brief
Professional
(MUST BE LEFT BLANK)
18 East 52nd Street, Lobby Rear, New York, NY 10022
(212)-584-MINT (6468)
info@brambletonassetsllc.example
Hey Designers, We would like for our telephone, fax, and email to be titled with symbols instead of words, e.g. a small telephone symbol next to the phone number and a fax machine next to the fax number. We require blank fields we can fill in, with no symbols, for: NAME, TITLE We require blank fields we can fill in, with symbols, for: CELL NUMBER, EMAIL, WEB ADDRESS Also, and this point is VERY IMPORTANT, we need the final deliverables to include an editable Adobe Illustrator and/or Photoshop file (preferably, Illustrator). We will include the names and titles of our individual employees ourselves, thus we need those sections to be left blank. All fields should be editable. We will not accept the design if it does not include a fully editable file. Our logo was recently completed and we require it to be included in the design. The file should be attached to the contest. We have additional versions of the logo we'd like to be able to swap out at will, however they are all in the same style as the logo provided, so the color scheme of the logo should be utilized throughout. The font should be traditional and corporate in style, and not too stylized or flashy. The logo should be included on the back as well. Thanks Everybody and Good Luck!

```html
<!DOCTYPE html>
<html lang="en">
<head>
<meta charset="utf-8">
<title>Brambleton Assets — Business Cards</title>
<link rel="stylesheet" href="https://fonts.googleapis.com/css2?family=Roboto:wght@400;700&display=swap">
<style>
  :root {
    --gold: #d9a21b;
    --gold-deep: #c28c10;
    --graphite: #6d6e70;
    --ink: #3a3a3c;
    --card: #ffffff;
    --backdrop: #e4e4e6;
  }
  html, body {
    margin: 0;
    padding: 0;
    width: 1200px;
    height: 799px;
    overflow: hidden;
    background: var(--backdrop);
    font-family: "Roboto", Arial, sans-serif;
  }
  .stage {
    position: relative;
    width: 1200px;
    height: 799px;
  }
  .card {
    position: absolute;
    top: 245px;
    width: 540px;
    height: 309px;
    background: var(--card);
    border-radius: 30px;
    box-shadow: 0 6px 22px rgba(0,0,0,0.18);
    overflow: hidden;
  }
  .card--back { left: 40px; }
  .card--front { left: 620px; }

  .brand {
    display: flex;
    align-items: center;
    gap: 10px;
    color: var(--gold);
    font-weight: 700;
    text-transform: uppercase;
    letter-spacing: 0.5px;
    white-space: nowrap;
  }
  .brand__mark {
    width: 34px;
    height: 34px;
    background: var(--gold);
    flex: none;
  }
  .brand__name { font-size: 30px; line-height: 1; }

  .card--back .brand {
    position: absolute;
    left: 0; right: 0;
    top: 102px;
    justify-content: center;
  }
  .social-row {
    position: absolute;
    left: 0; right: 0;
    top: 160px;
    display: flex;
    justify-content: center;
    gap: 8px;
  }
  .social-row__tile {
    width: 16px;
    height: 16px;
    border-radius: 3px;
    background: var(--gold);
  }
  .card--back .website {
    position: absolute;
    left: 0; right: 0;
    top: 190px;
    text-align: center;
    font-size: 13px;
    color: var(--ink);
  }

  .swoosh {
    position: absolute;
    left: 0; top: 0;
    width: 540px;
    height: 120px;
  }
  .card--front .brand {
    position: absolute;
    left: 118px;
    top: 132px;
  }
  .holder {
    position: absolute;
    right: 32px;
    top: 96px;
    text-align: left;
  }
  .holder__name {
    color: var(--gold);
    font-size: 16px;
    font-weight: 700;
    margin: 0;
  }
  .holder__title {
    color: var(--ink);
    font-size: 12px;
    margin: 3px 0 0;
  }
  .contact {
    position: absolute;
    left: 32px;
    bottom: 24px;
    margin: 0;
    padding: 0;
    list-style: none;
    font-size: 11.5px;
    line-height: 1.45;
    color: var(--ink);
  }
  .contact__label {
    color: var(--gold);
    font-weight: 700;
  }
</style>
</head>
<body>
<main class="stage">

  <section class="card card--back" aria-label="Card back">
    <div class="brand">
      <span class="brand__mark"></span>
      <span class="brand__name">Brambleton Assets</span>
    </div>
    <div class="social-row" aria-label="Social profiles">
      <span class="social-row__tile"></span>
      <span class="social-row__tile"></span>
      <span class="social-row__tile"></span>
      <span class="social-row__tile"></span>
      <span class="social-row__tile"></span>
    </div>
    <p class="website">www.brambletonassetsllc.example</p>
  </section>

  <section class="card card--front" aria-label="Card front">
    <svg class="swoosh" viewBox="0 0 540 120" aria-hidden="true">
      <path d="M0 0 H330 C250 20 170 55 0 95 Z" fill="var(--gold)"/>
      <path d="M0 98 C170 58 260 22 340 0 H352 C270 26 180 62 0 104 Z" fill="var(--graphite)"/>
    </svg>

    <div class="brand">
      <span class="brand__mark"></span>
      <span class="brand__name">Brambleton Assets</span>
    </div>

    <div class="holder">
      <p class="holder__name">Alex Morgan</p>
      <p class="holder__title">President</p>
    </div>

    <ul class="contact">
      <li>18 East 52nd Street, Lobby Rear, New York, NY 10022</li>
      <li><span class="contact__label">P:</span> (212)-584-MINT (6468), <span class="contact__label">C:</span> 555.555.5555, <span class="contact__label">F:</span> (212)-584-6469</li>
      <li><span class="contact__label">E:</span> info@brambletonassetsllc.example, <span class="contact__label">W:</span> www.brambletonassetsllc.example</li>
    </ul>
  </section>

</main>
</body>
</html>
```